Plakat-Design für Cloud-Telefonanlage
Zielgruppe
https://www.veltrano-beispiel.at/festnetz/business/virtuelle-cloud-telefonanlage
Aufgabenstellung
rollup_xxl_200x300 Grafik - siehe Datenblatt
Überschrift groß: Cloud Telefonanlage aus Tirol
Evt. dann die Features aufzählen [?] dazu hätte ich den Text u. die
Grafik im Anhang 'Cloud-Features' beigefügt.
**** Änderung am 17.06 **** : Die Features nur benennen, sprich ohne Beschreibung! Wird dann zu viel Inhalt.
Hinzufügen:
Computer Telefon Integration (CTI)
Konferenzen
Smartphone App
Sprachaufzeichnungen
Fax2Mail - Mail2Fax
Farbcode: A46CA0

```html
<!DOCTYPE html>
<html lang="de">
<head>
<meta charset="utf-8">
<title>Cloud Telefonanlage – Veltrano</title>
<link href="https://fonts.googleapis.com/css2?family=Montserrat:ital,wght@0,300;0,400;0,700;0,800;1,300;1,700;1,800&display=swap" rel="stylesheet">
<style>
  :root {
    --brand: #a46ca0;
    --ink: #111111;
    --text: #2a2a2a;
    --paper: #ffffff;
  }
  * { margin: 0; padding: 0; box-sizing: border-box; }
  html, body { width: 750px; height: 1200px; overflow: hidden; background: var(--paper); }
  body { font-family: "Montserrat", sans-serif; color: var(--text); }
  .poster { position: relative; width: 750px; height: 1200px; }

  .brand-name {
    position: absolute; right: 50px; top: 48px;
    display: flex; align-items: center; gap: 10px;
    font-weight: 800; font-size: 38px; line-height: 1; color: var(--ink);
  }
  .brand-square { width: 14px; height: 14px; background: var(--brand); }

  .headline { position: absolute; left: 68px; top: 124px; line-height: 1; }
  .headline-light {
    display: block; font-weight: 300; font-size: 44px;
    letter-spacing: 5px; color: var(--ink);
  }
  .headline-bold {
    display: block; margin-top: 4px; font-weight: 800; font-size: 42px;
    letter-spacing: 3.6px; color: var(--ink);
  }
  .headline-rule {
    position: absolute; left: 0; top: 243px; width: 367px; height: 3px;
    background: var(--brand);
  }
  .headline-origin {
    position: absolute; left: 381px; top: 233px;
    font-style: italic; font-weight: 300; font-size: 19px; line-height: 1.2;
    color: var(--brand); letter-spacing: 0.5px;
  }

  .feature-list {
    position: absolute; left: 59px; top: 350px; width: 650px;
    list-style: none;
    display: grid; grid-template-columns: 356px 1fr;
    grid-auto-rows: 84px;
  }
  .feature {
    display: flex; align-items: center; gap: 12px; height: 28px;
    font-weight: 800; font-style: italic; font-size: 16px; color: var(--ink);
  }
  .feature-icon { width: 21px; height: 21px; flex: none; fill: var(--brand); }
</style>
</head>
<body>
<main class="poster">
  <div class="brand-name"><span class="brand-square"></span>Veltrano</div>

  <h1 class="headline">
    <span class="headline-light">CLOUD</span>
    <span class="headline-bold">TELEFONANLAGE</span>
  </h1>
  <div class="headline-rule"></div>
  <div class="headline-origin">AUS TIROL</div>

  <ul class="feature-list">
    <li class="feature"><svg class="feature-icon" viewBox="0 0 24 24"><path d="M6.6 10.8a15.1 15.1 0 0 0 6.6 6.6l2.2-2.2c.3-.3.7-.4 1-.2 1.1.4 2.3.6 3.6.6.6 0 1 .4 1 1V20c0 .6-.4 1-1 1A17 17 0 0 1 3 4c0-.6.4-1 1-1h3.5c.6 0 1 .4 1 1 0 1.3.2 2.5.6 3.6.1.3 0 .7-.2 1z"/></svg>Telefoniefunktion</li>
    <li class="feature"><svg class="feature-icon" viewBox="0 0 24 24"><path d="M9 2h6v6h-2v3h8v5h2v6h-6v-6h2v-3h-6v3h2v6H9v-6h2v-3H5v3h2v6H1v-6h2v-5h8V8H9z"/></svg>Durchwahlen Verwaltung</li>

    <li class="feature"><svg class="feature-icon" viewBox="0 0 24 24"><path d="M9 4H5a2 2 0 0 0-2 2v12a2 2 0 0 0 2 2h4v-3H6V7h3zm5 1v4H9v6h5v4l8-7z"/></svg>Routing &amp; Weiterleitungen</li>
    <li class="feature"><svg class="feature-icon" viewBox="0 0 24 24"><path d="M12 2a10 10 0 1 0 0 20 10 10 0 0 0 0-20zm0 2a8 8 0 1 1 0 16 8 8 0 0 1 0-16zm-1 3v6l5 3 1-1.6-4-2.4V7z"/></svg>Geschäftszeiten</li>

    <li class="feature"><svg class="feature-icon" viewBox="0 0 24 24"><circle cx="12" cy="8" r="3.5"/><circle cx="5" cy="9" r="2.5"/><circle cx="19" cy="9" r="2.5"/><path d="M5 19c0-3.5 3-6 7-6s7 2.5 7 6zM0 18c0-2.5 2-4.5 5-4.5l1 .1A8 8 0 0 0 3.5 18zM24 18c0-2.5-2-4.5-5-4.5l-1 .1a8 8 0 0 1 2.5 4.4z"/></svg>Anrufgruppen</li>
    <li class="feature"><svg class="feature-icon" viewBox="0 0 24 24"><path d="M3 5h18v2.5H3zm0 5.75h18v2.5H3zm0 5.75h18V19H3z"/></svg>IVR-Menü</li>

    <li class="feature"><svg class="feature-icon" viewBox="0 0 24 24"><path d="M20 3v18l-7-4H9l1 5H6l-1-5H3V7h10zm-3 4-4 2H5v6h8l4 2z"/></svg>Ansagen</li>
    <li class="feature"><svg class="feature-icon" viewBox="0 0 24 24"><path d="M7 10V7a5 5 0 0 1 10 0v3h2v12H5V10zm3 0h4V7a2 2 0 0 0-4 0z"/></svg>Anrufsperren &amp; Gesprächslimit</li>

    <li class="feature"><svg class="feature-icon" viewBox="0 0 24 24"><path d="M5 5h14l3 8v6H2v-6zm1.5 2L4.5 12H9l1 2h4l1-2h4.5l-2-5z"/></svg>Virtuelle Sprachbox (Voice2Mail)</li>
    <li class="feature"><svg class="feature-icon" viewBox="0 0 24 24"><path d="M4 2h14a2 2 0 0 1 2 2v16a2 2 0 0 1-2 2H4zm7 5a2.5 2.5 0 1 0 0 5 2.5 2.5 0 0 0 0-5zm-4.5 10h9c0-2.5-2-4-4.5-4s-4.5 1.5-4.5 4zM21 5h1.5v3H21zm0 5h1.5v3H21z"/></svg>Globales Telefonbuch</li>

    <li class="feature"><svg class="feature-icon" viewBox="0 0 24 24"><path d="M6.6 10.8a15.1 15.1 0 0 0 6.6 6.6l2.2-2.2c.3-.3.7-.4 1-.2 1.1.4 2.3.6 3.6.6.6 0 1 .4 1 1V20c0 .6-.4 1-1 1A17 17 0 0 1 3 4c0-.6.4-1 1-1h3.5c.6 0 1 .4 1 1 0 1.3.2 2.5.6 3.6.1.3 0 .7-.2 1z"/><path d="M20.5 2 22 3.5 3.5 22 2 20.5z"/></svg>Verpasste Anrufe &amp; Logs</li>
    <li class="feature"><svg class="feature-icon" viewBox="0 0 24 24"><path d="M2 3h2v16h18v2H2zm5 8h2.5v6H7zm4-3h2.5v9H11zm4 2h2.5v7H15zm4-4h2.5v11H19z"/></svg>Anrufstatistiken</li>

    <li class="feature"><svg class="feature-icon" viewBox="0 0 24 24"><path d="M2 3h20v13H2zm2 2v9h16V5zM9 18h6v2h3v2H6v-2h3z"/></svg>Computer Telefon Integration (CTI)</li>
    <li class="feature"><svg class="feature-icon" viewBox="0 0 24 24"><circle cx="8" cy="8" r="3.5"/><circle cx="16.5" cy="8" r="3.5"/><path d="M1 20c0-4 3-6.5 7-6.5s7 2.5 7 6.5zm15-6.5c4 0 7 2.5 7 6.5h-6c0-2.5-1-4.8-3-6.2z"/></svg>Konferenzen</li>

    <li class="feature"><svg class="feature-icon" viewBox="0 0 24 24"><path d="M7 1h10a2 2 0 0 1 2 2v18a2 2 0 0 1-2 2H7a2 2 0 0 1-2-2V3a2 2 0 0 1 2-2zm0 3v14h10V4zm5 15.5a1.2 1.2 0 1 0 0 2.4 1.2 1.2 0 0 0 0-2.4z"/></svg>Smartphone App</li>
    <li class="feature"><svg class="feature-icon" viewBox="0 0 24 24"><path d="M12 1a4 4 0 0 1 4 4v6a4 4 0 0 1-8 0V5a4 4 0 0 1 4-4zM5 10h2a5 5 0 0 0 10 0h2a7 7 0 0 1-6 6.9V20h3v2H8v-2h3v-3.1A7 7 0 0 1 5 10z"/></svg>Sprachaufzeichnungen</li>

    <li class="feature"><svg class="feature-icon" viewBox="0 0 24 24"><path d="M2 4h20v16H2zm2.5 2 7.5 6 7.5-6zM4 8v10h16V8l-8 6.4z"/></svg>Fax2Mail – Mail2Fax</li>
  </ul>
</main>
</body>
</html>
```